App Design Project

Hello,
I'm looking for a great designer for my iOS Applications, we have a lot of works and we're short in designers :(
I want to revamp my thermometer iOS app. You will find attached the images I want to replace. I need something with the same element (temp, condition, weather icon) but with a different look!
Same, new icon, you have carte blanche to this one.
I want a design that stands out from the hundreds of weather application that almost all the same design. I am looking for something that does say "wow, it rocks."
Please do not Provide classic design that we can see everywhere ... I'm looking for something with a real artistic choice, contrast, colours, etc.
As a marketing screenshot, I want something classic, you'll find an example attached, feel free to innovate.
To sum-up :
- One new view for my App
- One new icon
- One marketing screenshot

```html
<!DOCTYPE html>
<html lang="en">
<head>
<meta charset="utf-8">
<title>Hail – Weather View</title>
<link href="https://fonts.googleapis.com/css2?family=Jost:wght@600;700&family=Raleway:wght@100&family=Roboto:wght@400&family=Noto+Serif:ital,wght@1,700&display=swap" rel="stylesheet">
<style>
  :root {
    --canvas: #e4e4e4;
    --ink: #1a1a1a;
    --paper: #ffffff;
    --paper-shade: #ececec;
    --hail-light: #d9d6d3;
    --hail-mid: #bdb5b0;
    --hail-warm: #b79f96;
  }
  html, body {
    margin: 0;
    width: 1200px;
    height: 1200px;
    overflow: hidden;
    background: var(--canvas);
  }
  .weather-view {
    position: absolute;
    left: 320px;
    top: 67px;
    width: 400px;
    height: 762px;
    transform: scale(1.4);
    transform-origin: 0 0;
    overflow: hidden;
    color: var(--ink);
  }
  .weather-view svg { position: absolute; inset: 0; }
  .condition {
    position: absolute;
    left: 76px;
    top: 88px;
    margin: 0;
    font: 100 66px/1 "Raleway", sans-serif;
    letter-spacing: -1px;
  }
  .conditions-detail {
    position: absolute;
    left: 73px;
    top: 203px;
    margin: 0;
    font: 400 16.5px/28px "Roboto", sans-serif;
    letter-spacing: 0.3px;
  }
  .temp-celsius {
    position: absolute;
    left: 50px;
    top: 272px;
    margin: 0;
    font: 700 142px/1 "Jost", sans-serif;
    letter-spacing: -2px;
  }
  .temp-celsius .unit {
    font-size: 68px;
    vertical-align: 58px;
    letter-spacing: 0;
  }
  .temp-fahrenheit {
    position: absolute;
    left: 52px;
    top: 463px;
    margin: 0;
    font: 600 50px/1 "Jost", sans-serif;
    letter-spacing: 4px;
  }
  .info-button {
    position: absolute;
    left: 370px;
    top: 692px;
    font: italic 700 30px/1 "Noto Serif", serif;
  }
</style>
</head>
<body>
  <main class="weather-view">
    <svg width="400" height="762" viewBox="0 0 400 762" aria-hidden="false">
      <defs>
        <linearGradient id="hail-backdrop" x1="0" y1="0" x2="0.3" y2="1">
          <stop offset="0" stop-color="var(--hail-light)"/>
          <stop offset="0.45" stop-color="var(--hail-mid)"/>
          <stop offset="1" stop-color="var(--hail-warm)"/>
        </linearGradient>
        <linearGradient id="temp-band" x1="0" y1="0" x2="0" y2="1">
          <stop offset="0" stop-color="#f4f4f4"/>
          <stop offset="1" stop-color="#ffffff"/>
        </linearGradient>
      </defs>
      <rect class="hail-photo" width="400" height="762" fill="url(#hail-backdrop)" role="img" aria-label="Photograph of hailstones falling against a soft grey and pink backdrop"/>
      <!-- folded paper panels -->
      <rect class="fold-top" x="228" y="0" width="172" height="200" fill="var(--paper)"/>
      <polygon class="fold-side" points="228,200 400,200 400,280 228,280" fill="var(--paper-shade)"/>
      <polygon class="fold-diagonal" points="400,105 400,200 300,220" fill="#f7f7f7"/>
      <polygon class="fold-arrow" points="228,165 300,220 228,280" fill="#f2f2f2"/>
      <rect class="temp-band" x="0" y="280" width="400" height="158" fill="url(#temp-band)"/>
      <polygon class="band-shade-left" points="0,300 110,438 0,438" fill="#ebebeb"/>
      <polygon class="band-shade-right" points="400,290 310,438 400,438" fill="#eeeeee"/>
      <polygon class="fold-chevron" points="0,438 345,438 140,600" fill="rgba(255,255,255,0.32)"/>
      <line class="divider" x1="0" y1="438.5" x2="345" y2="438.5" stroke="var(--ink)" stroke-width="1"/>
      <g class="refresh-icon" transform="translate(378 446)" fill="none" stroke="var(--ink)" stroke-width="3.2">
        <path d="M-3 -8 A8 8 0 1 1 -8 2"/>
        <polygon points="-9,-12 -1,-9 -7,-3" fill="var(--ink)" stroke="none"/>
      </g>
    </svg>

    <h1 class="condition">HAIL</h1>
    <p class="conditions-detail">HUMIDITY: 87%<br>N/NW AT 8 MPH</p>
    <p class="temp-celsius">28<span class="unit">°C</span></p>
    <p class="temp-fahrenheit">82.4 °F</p>
    <span class="info-button">i</span>
  </main>
</body>
</html>
```